MARLO Real Estate Prospecting DL Flyer

I need a DL size (99mm x 210mm) two sided flyer designed for letter boxing and also handing to prospective clients when door knocking across my sales area in Melbourne, Australia. PLEASE NOTE: the flyer is a flat flyer to be designed on both sides as per my doc below. The flyer will likely be printed on 350gsm card. It will not be posted - so NO space for address required. It is for door-knocking (door to door sales) and letter boxing (dropped personally by me in a letterbox - not posted).
My original company logo design brief was that it should be modern and premium black on white and white on black - drawing influences by FELIX DORNE and also CALISTA. I want my DL flyer to reflect the same influence. I have attached proposed copy on the word document attached below.
The DL flyer will be printed on 350 gsm - probably gloss to reflect the premium feel, but open to suggestion. It is important for the flyer to be durable and have decent shelf life - I am not going for cheap and cheerful on this project. I need to make an impact. I am trying to attract home owners to my business to list and sell their properties - usually for most people their biggest asset is their home/property - so it is important that my business is credible and very experienced (which of course it is).
For a view of the types of properties I sell please go to www.homelistingsdemo.com.au and type in Mount Waverley, Victoria; and also Glen Waverley, Victoria. You will see a list of properties come up that are either for SALE or for SALE BY AUCTION. This may help with your understanding. The areas I concentrate on are very suburban - meaning families, families, families :)

Target Market(s)

Property owners across the middle ring of eastern suburbs of Melbourne. Value of homes are between $1m and $2m, and mostly consist of 3 and 4 bedroom family homes. Clients range from the elderly looking to downsize to a smaller property, to families looking to sell and upgrade their homes.

Industry/Entity Type

Real Estate Agent

Font styles to use
Serif

Colors
000000
ffffff

Requirements
Must have
• The "call to action" components that I have included on the doc file and include a FREE E-BOOK on supply of their contact details; and a FREE PROFESSIONAL HOME STYLIST CONSULTATION.
• It must feature my company logo. My corporate colours are black and white - so best to stick with these in the design.
• UPDATE: Just call the e-book "5 EASY STEPS TO LIFT THE FINAL OFFER ON YOUR HOUSE"
• ...forget the City of Brellton and City of Parkvane part!!
• UPDATE: Designs I have liked the best include the following elements:
• 1. Strong brand at top of each side of flyer
• 2. Family pic page 1; property pic page 2
• 3. BOLD Headings
• 4. Amplified CALL TO ACTION - FREE......consult; FREE E-Book
• 5. Clear visible contact details at bottom of page
Nice to have
• Lifestyle photography of homes.
• Some designers have used Asian families in their pics - which is smart as the main buyer demographic is Chinese families. The mail ownership is Australian - so a mix of Asian and Anglo is fine. Try and avoid overtly USA style properties - as Melbourne styles are different. Keys, handshakes etc are all good :)
Should not have
• Animation, cartoons, or visual drawings included.

```html
<!DOCTYPE html>
<html lang="en">
<head>
<meta charset="utf-8">
<title>MARLO Real Estate – DL Flyer</title>
<link rel="stylesheet" href="https://fonts.googleapis.com/css2?family=Open+Sans:wght@400;600;700;800&family=Roboto+Condensed:wght@700&display=swap">
<style>
  :root{
    --ink:#111111;
    --charcoal:#2b2b2b;
    --text:#222222;
    --paper:#ffffff;
    --backdrop:#e6e2dc;
  }
  *{box-sizing:border-box;margin:0;padding:0}
  html,body{width:1200px;height:1012px;overflow:hidden}
  body{background:var(--backdrop);font-family:"Open Sans",Arial,sans-serif;color:var(--text);position:relative}
  .flyer{position:absolute;top:86px;width:400px;height:840px;background:var(--paper);overflow:hidden;box-shadow:0 4px 14px rgba(0,0,0,.25)}
  .flyer--front{left:161px}
  .flyer--back{left:644px}
  .abs{position:absolute}

  .brand{position:absolute;left:0;width:100%;text-align:center}
  .brand__name{font-family:"Open Sans",Arial,sans-serif;font-weight:700;font-size:66px;line-height:1;letter-spacing:2px;color:var(--charcoal)}
  .brand__sub{font-family:"Open Sans",Arial,sans-serif;font-weight:400;font-size:13px;letter-spacing:11px;color:var(--charcoal);margin-top:6px;padding-left:11px}

  /* front */
  .front__header{left:0;top:0;width:400px;height:260px;background:linear-gradient(180deg,#ffffff 0%,#d8d8d8 55%,#bdbdbd 100%)}
  .front__photo{left:0;top:0;width:400px;height:400px}
  .front__headline{top:372px;left:0;width:400px;text-align:center;font-weight:800;font-size:22px;line-height:25px;color:var(--charcoal)}
  .front__tagline{top:425px;left:22px;width:330px;font-size:10.5px;line-height:14px}
  .front__intro{top:466px;left:22px;width:358px;font-size:12px;line-height:17.5px;text-align:justify}
  .front__intro b{font-weight:800}
  .benefits{top:558px;left:22px;width:358px;list-style:none;font-size:12px;line-height:17px}
  .benefits li{position:relative;padding-left:22px;margin-bottom:2px}
  .benefits li::before{content:"";position:absolute;left:4px;top:6px;width:6px;height:6px;border-radius:50%;background:var(--ink)}
  .ebook-btn{top:672px;left:48px;width:290px;height:22px;border-radius:5px;background:var(--charcoal);color:var(--paper);font-family:"Roboto Condensed",Arial,sans-serif;font-weight:700;font-size:15px;line-height:22px;text-align:center}
  .ebook-title{top:704px;left:22px;width:360px;font-weight:800;font-size:11.5px;line-height:16px;color:var(--charcoal)}
  .front__footer{left:0;top:752px;width:400px;height:88px}
  .front__call{top:770px;left:0;width:400px;text-align:center;font-family:"Roboto Condensed",Arial,sans-serif;font-weight:700;font-size:30px;color:var(--paper)}
  .email{left:0;width:400px;text-align:center;color:var(--paper);font-size:11.5px;font-weight:600;display:flex;justify-content:center;align-items:center;gap:5px}
  .front__email{top:818px}

  /* back */
  .back__photo{left:0;top:0;width:400px;height:240px}
  .back__headline{top:318px;left:0;width:400px;text-align:center;font-weight:800;font-size:17px;color:var(--ink)}
  .back__portrait{top:369px;left:28px;width:116px;height:222px}
  .back__bio{top:350px;left:160px;width:220px;font-size:12.3px;line-height:16.7px;text-align:justify}
  .back__offer{top:610px;left:22px;width:360px;font-size:12.3px;line-height:17px}
  .back__offer b{font-weight:800;font-size:14px}
  .call-box{top:688px;left:22px;width:350px;height:106px;border-radius:9px;background:linear-gradient(180deg,#f4f4f4 0%,#d9d9d9 45%,#b9b9b9 100%);text-align:center;font-family:"Roboto Condensed",Arial,sans-serif;font-weight:700;color:var(--charcoal)}
  .call-box__label{font-size:30px;margin-top:4px}
  .call-box__number{font-size:46px;line-height:52px}
  .back__footer{left:0;top:815px;width:400px;height:25px;background:var(--charcoal)}
  .back__email{top:819px}
</style>
</head>
<body>

<section class="flyer flyer--front" aria-label="Flyer front">
  <div class="abs front__header"></div>
  <svg class="abs front__photo" viewBox="0 0 400 400" role="img" aria-label="Photo of a smiling family of four at home">
    <defs>
      <linearGradient id="familyTone" x1="0" y1="0" x2="0" y2="1">
        <stop offset="0" stop-color="#e9e6e3"/>
        <stop offset="0.5" stop-color="#e0c9b4"/>
        <stop offset="1" stop-color="#f4f1ee"/>
      </linearGradient>
    </defs>
    <polygon points="0,228 200,140 400,228 400,392 0,392" fill="url(#familyTone)"/>
    <polyline points="0,236 200,132 400,236" fill="none" stroke="#262626" stroke-width="13"/>
  </svg>
  <div class="brand" style="top:36px">
    <div class="brand__name">MARLO</div>
    <div class="brand__sub">REAL ESTATE</div>
  </div>

  <h1 class="abs front__headline">GET THE MAXIMUM PRICE<br>FOR YOUR PROPERTY</h1>
  <p class="abs front__tagline">Personal Service, Clear Communication, Honest Advice, Top Results, For A Flat Fee</p>
  <p class="abs front__intro">At <b>MARLO</b> Real Estate we are doing things differently. Our property sales process is designed to extract an <b>ELITE LEVEL PRICE</b> for you, but our cost of doing business is significantly reduced from that of our competitors, and that results in <b>MORE MONEY IN YOUR POCKET.</b></p>
  <ul class="abs benefits">
    <li>ELITE sales process ensures the maximum possible price for your property.</li>
    <li>Low FLAT FEE selling commission – up to half that charged by other agents.</li>
    <li>A FLAT FEE in high impact marketing for the sale of your home.</li>
  </ul>
  <div class="abs ebook-btn">GET YOUR FREE COPY OF MY E-BOOK</div>
  <p class="abs ebook-title">"5 EASY STEPS TO LIFT THE FINAL OFFER ON YOUR HOUSE"</p>

  <svg class="abs front__footer" viewBox="0 0 400 88" aria-hidden="true">
    <defs>
      <linearGradient id="swoosh" x1="0" y1="0" x2="1" y2="0">
        <stop offset="0" stop-color="#ffffff"/>
        <stop offset="0.6" stop-color="#bdbdbd"/>
        <stop offset="1" stop-color="#8c8c8c"/>
      </linearGradient>
    </defs>
    <path d="M0,18 Q200,-4 400,4 L400,22 Q200,12 0,22 Z" fill="url(#swoosh)"/>
    <path d="M0,22 Q200,10 400,16 L400,88 L0,88 Z" fill="#262626"/>
  </svg>
  <div class="abs front__call">Call Now:1800 555 019</div>
  <div class="abs email front__email">
    <svg width="12" height="12" viewBox="0 0 12 12" aria-hidden="true"><circle cx="6" cy="6" r="6" fill="#fff"/><rect x="2.5" y="3.8" width="7" height="4.6" fill="#262626"/><polyline points="2.5,3.8 6,6.5 9.5,3.8" fill="none" stroke="#fff" stroke-width=".8"/></svg>
    sales@marlorealestate.com.au
  </div>
</section>

<section class="flyer flyer--back" aria-label="Flyer back">
  <svg class="abs back__photo" viewBox="0 0 400 240" role="img" aria-label="Photo of a two-storey family home under a blue sky">
    <defs>
      <linearGradient id="homeTone" x1="0" y1="0" x2="0" y2="1">
        <stop offset="0" stop-color="#5f93d6"/>
        <stop offset="0.35" stop-color="#b9cfe6"/>
        <stop offset="0.6" stop-color="#b7a98c"/>
        <stop offset="0.82" stop-color="#8d9a6c"/>
        <stop offset="1" stop-color="#ffffff"/>
      </linearGradient>
    </defs>
    <rect width="400" height="240" fill="url(#homeTone)"/>
  </svg>
  <div class="brand" style="top:200px">
    <div class="brand__name">MARLO</div>
    <div class="brand__sub">REAL ESTATE</div>
  </div>
  <h2 class="abs back__headline">A DECADE OF EXPERIENCE ON YOUR SIDE</h2>
  <svg class="abs back__portrait" viewBox="0 0 116 222" role="img" aria-label="Portrait photo of the agent in a dark suit">
    <defs>
      <linearGradient id="agentTone" x1="0" y1="0" x2="0" y2="1">
        <stop offset="0" stop-color="#ffffff"/>
        <stop offset="0.3" stop-color="#a9a9ae"/>
        <stop offset="1" stop-color="#202228"/>
      </linearGradient>
    </defs>
    <rect width="116" height="222" fill="url(#agentTone)"/>
  </svg>
  <p class="abs back__bio">My name's Daniel Marlo. With over a decade of experience in the property industry I know what it takes to get you the BEST POSSIBLE PRICE for your property. I've spent much of my career in the cutthroat world of commercial property and closing high stakes international real estate deals. But 3 years ago I brought my expertise home to focus on the communities in Melbourne's eastern suburbs. I've had many incredible sales results to date. Will yours be next?</p>
  <p class="abs back__offer">Claim Your Free Property Market Appraisal Now And Receive A BONUS Professional Home Stylist Consultation – Normally Worth <b>$118</b></p>
  <div class="abs call-box">
    <div class="call-box__label">Call Now</div>
    <div class="call-box__number">1800 555 019</div>
  </div>
  <div class="abs back__footer"></div>
  <div class="abs email back__email">
    <svg width="12" height="12" viewBox="0 0 12 12" aria-hidden="true"><circle cx="6" cy="6" r="6" fill="#fff"/><rect x="2.5" y="3.8" width="7" height="4.6" fill="#262626"/><polyline points="2.5,3.8 6,6.5 9.5,3.8" fill="none" stroke="#fff" stroke-width=".8"/></svg>
    sales@marlorealestate.com.au
  </div>
</section>

</body>
</html>
```